Varnek Power Services Website - Solar Sales and Installation and Renewable Energy Marketing

I need a website for my solar sales and installation/renewable energy marketing company. We will focus on solar, so the web page should make that a main focus. Ideally it will have 5-6 total pages. One main page, one page "Why Solar", "Our Services", "About Us", "Contact Us", and some type of page that collects leads or information from customers who are interested in a solar quote. Our image focus should be either residential solar panels or windmills (renewable energy). The logo, attached, is green and orange. The color scheme should be predominantly white, clean cut, with orange/green buttons or accents. I don't want to have a blog-like page, it should mimic other solar company websites. A good example would be Truloka's solar website.

```html
<!DOCTYPE html>
<html lang="en">
<head>
<meta charset="utf-8">
<title>Varnek Power Services – Solar Sales &amp; Installation</title>
<link rel="stylesheet" href="https://fonts.googleapis.com/css2?family=Oswald:wght@400;500&family=Ubuntu:wght@400;500&family=Mulish:wght@400;500&display=swap">
<style>
:root{
  --orange:#ff6f00;
  --lime:#a6ff00;
  --ink:#222222;
  --text:#555555;
  --muted:#777777;
  --line:#cfcfcf;
  --soft:#f5f5f5;
  --footer:#1c1c1c;
  --footer-deep:#111111;
  --social:#1f6fd6;
}
*{margin:0;padding:0;box-sizing:border-box}
html,body{width:1200px;height:3516px;overflow:hidden}
body{position:relative;background:#fff;font-family:"Mulish",sans-serif;color:var(--text)}
.abs{position:absolute}
.btn{position:absolute;background:var(--orange);color:#fff;font-family:"Mulish",sans-serif;font-size:20px;display:flex;align-items:center;justify-content:center;border-radius:3px;text-transform:uppercase}

/* header */
.site-header{position:absolute;left:0;top:0;width:1200px;height:83px;background:#fff}
.brand{position:absolute;left:76px;top:14px;display:flex;align-items:center;gap:10px}
.brand-dot{width:50px;height:50px;border-radius:50%;background:var(--lime)}
.brand-name{font-family:"Ubuntu",sans-serif;font-weight:500;font-size:11px;line-height:13px;color:var(--ink);text-transform:uppercase;border-left:1px solid var(--ink);padding-left:8px}
.nav{position:absolute;top:30px;font-family:"Mulish",sans-serif;font-size:16px;color:var(--text)}
.nav.active{color:var(--orange)}
.nav-sep{position:absolute;left:967px;top:27px;width:1px;height:28px;background:#ddd}
.phone{position:absolute;left:986px;top:29px;font-size:18px;color:var(--orange);font-weight:500;display:flex;gap:8px;align-items:center}

/* hero */
.hero{position:absolute;left:0;top:83px;width:1200px;height:594px;background:linear-gradient(100deg,#3d3027 0%,#5a4636 35%,#8a6a52 60%,#6b5444 85%,#4a3a2e 100%)}
.hero-kicker{position:absolute;left:76px;top:240px;font-family:"Oswald",sans-serif;font-size:54px;color:#fff;line-height:1}
.hero-title{position:absolute;left:78px;top:300px;font-family:"Oswald",sans-serif;font-weight:500;font-size:82px;color:#fff;line-height:1}
.hero-copy{position:absolute;left:79px;top:398px;width:440px;font-size:17px;line-height:25px;color:#fff}
.slider-arrow{position:absolute;top:354px;width:46px;height:46px;border-radius:50%;background:rgba(0,0,0,.35);display:flex;align-items:center;justify-content:center}

/* headings */
.section-title{position:absolute;font-family:"Ubuntu",sans-serif;font-weight:500;font-size:40px;color:var(--ink);line-height:1;padding-left:22px;text-transform:uppercase}
.section-title::before{content:"";position:absolute;left:0;top:2px;width:3px;height:38px;background:var(--orange)}

/* why solar */
.feature{position:absolute;top:820px;width:240px;text-align:center}
.feature svg{display:block;margin:0 auto}
.feature h3{font-family:"Ubuntu",sans-serif;font-weight:400;font-size:20px;color:var(--ink);margin-top:26px}
.feature p{font-size:14px;line-height:25px;color:var(--muted);margin-top:12px}

/* about */
.about{position:absolute;left:0;top:1084px;width:1200px;height:520px;background:var(--soft)}
.about-title{position:absolute;left:78px;top:1158px;font-family:"Ubuntu",sans-serif;font-weight:500;font-size:40px;line-height:47px;color:var(--ink);padding-left:22px;text-transform:uppercase}
.about-title::before{content:"";position:absolute;left:0;top:0;width:3px;height:38px;background:var(--orange)}
.about-copy{position:absolute;left:104px;top:1267px;width:450px;font-size:13.5px;line-height:27px;color:var(--text)}
.about-copy p+p{margin-top:14px}
.photo{position:absolute}

/* services */
.services-lead{position:absolute;left:0;top:1722px;width:1200px;text-align:center;font-size:16px;color:var(--text)}
.tile{position:absolute;top:1832px;width:238px;height:274px}
.tile .tile-photo{position:absolute;left:0;top:0;width:100%;height:218px}
.tile .tile-label{position:absolute;left:0;bottom:0;width:100%;height:56px;background:var(--lime);color:var(--ink);font-size:17px;display:flex;align-items:center;justify-content:center}
.tile.featured{top:1811px;height:316px}
.tile.featured .tile-photo{height:261px}
.tile.featured .tile-label{height:55px;background:var(--orange);color:#fff}

/* choose */
.choose-title{position:absolute;left:669px;top:2208px;font-family:"Ubuntu",sans-serif;font-weight:500;font-size:40px;line-height:47px;color:var(--ink);padding-left:18px}
.choose-title::before{content:"";position:absolute;left:0;top:4px;width:3px;height:38px;background:var(--orange)}
.choose-title .accent{color:var(--orange)}
.choose-copy{position:absolute;left:689px;top:2364px;width:360px;font-size:13.5px;line-height:27px;color:var(--text)}

/* contact */
.contact-lead{position:absolute;left:0;top:2651px;width:1200px;text-align:center;font-size:16px;color:var(--ink)}
.contact-lead a{color:var(--orange)}
.contact-fade{position:absolute;left:0;top:3000px;width:1200px;height:183px;background:linear-gradient(180deg,#fff 0%,#eeeeee 100%)}
.field-label{position:absolute;font-size:13px;color:var(--text)}
.field{position:absolute;border:1px solid var(--line);background:#fff}

/* footer */
.site-footer{position:absolute;left:0;top:3183px;width:1200px;height:333px;background:var(--footer)}
.footer-brand{position:absolute;left:108px;top:3250px;display:flex;align-items:center;gap:14px}
.footer-brand .brand-dot{width:72px;height:72px}
.footer-brand .brand-name{font-size:17px;line-height:20px;color:#fff;border-left:1px solid #fff;padding-left:10px;letter-spacing:1px}
.social{position:absolute;top:3359px;width:42px;height:42px;border-radius:50%;background:var(--social)}
.footer-col{position:absolute;top:3218px}
.footer-col h4{font-family:"Ubuntu",sans-serif;font-weight:400;font-size:20px;color:#fff;margin-bottom:16px}
.footer-col li{list-style:none;font-size:13.5px;color:#cfcfcf;height:33px;padding-left:22px;position:relative}
.footer-col li::before{content:"";position:absolute;left:0;top:6px;width:6px;height:6px;border-radius:50%;background:var(--orange)}
.contact-row{display:flex;gap:18px;font-size:13.5px;line-height:22px;color:#cfcfcf;margin-bottom:18px}
.copyright{position:absolute;left:0;top:3454px;width:1200px;height:62px;background:var(--footer-deep);color:#cfcfcf;font-size:14px;display:flex;align-items:center;justify-content:center}
.copyright .accent{color:var(--orange);margin:0 4px}
</style>
</head>
<body>

<header class="site-header">
  <div class="brand"><span class="brand-dot"></span><span class="brand-name">Varnek<br>Power<br>Services</span></div>
  <span class="nav active" style="left:457px">Home ▾</span>
  <span class="nav" style="left:541px">Why Solar</span>
  <span class="nav" style="left:643px">Our Services</span>
  <span class="nav" style="left:764px">About Us</span>
  <span class="nav" style="left:858px">Contact Us</span>
  <span class="nav-sep"></span>
  <span class="phone">
    <svg width="18" height="18" viewBox="0 0 24 24"><path d="M6.6 10.8a15 15 0 0 0 6.6 6.6l2.2-2.2a1 1 0 0 1 1-.25 11.4 11.4 0 0 0 3.6.57 1 1 0 0 1 1 1V20a1 1 0 0 1-1 1A17 17 0 0 1 3 4a1 1 0 0 1 1-1h3.5a1 1 0 0 1 1 1c0 1.25.2 2.45.57 3.57a1 1 0 0 1-.25 1z" fill="currentColor"/></svg>
    123.456.7890
  </span>
</header>

<section class="hero" role="img" aria-label="Smiling family with a child on a father's back in front of houses with solar roofs">
</section>
<div class="hero-kicker">Make The Sun</div>
<div class="hero-title">Work For You</div>
<p class="hero-copy">Lorem Ipsum is simply dummy text of the printing and type setting has been the industry's</p>
<div class="btn" style="left:76px;top:463px;width:261px;height:52px">Get Started With Us</div>
<div class="slider-arrow" style="left:13px"><svg width="14" height="20" viewBox="0 0 14 20"><path d="M10 2 3 10l7 8" stroke="#fff" stroke-width="1.5" fill="none"/></svg></div>
<div class="slider-arrow" style="left:1139px"><svg width="14" height="20" viewBox="0 0 14 20"><path d="m4 2 7 8-7 8" stroke="#fff" stroke-width="1.5" fill="none"/></svg></div>

<h2 class="section-title" style="left:483px;top:742px">Why Solar</h2>

<div class="feature" style="left:85px">
  <svg width="74" height="66" viewBox="0 0 74 66" fill="none" stroke="var(--orange)" stroke-width="2.5" stroke-linejoin="round">
    <rect x="6" y="30" width="14" height="30"/>
    <path d="M20 32 34 16V4c6 0 9 5 7 14l-2 8h20a5 5 0 0 1 0 10h-2a5 5 0 0 1 0 10h-2a5 5 0 0 1 0 10H38c-7 0-12-2-18-4"/>
  </svg>
  <h3>Simple and Easy</h3>
  <p>Lorem Ipsum is simply dummy text of the printing and type setting has been the industry's</p>
</div>
<div class="feature" style="left:344px">
  <svg width="70" height="66" viewBox="0 0 70 66" fill="none" stroke="var(--orange)" stroke-width="2.5" stroke-linejoin="round">
    <path d="M10 18 40 6l6 12"/>
    <rect x="6" y="18" width="56" height="40" rx="3"/>
    <path d="M62 30H46a6 6 0 0 0 0 12h16z"/>
    <circle cx="48" cy="36" r="2" fill="var(--orange)"/>
    <path d="M10 24h4M18 24h4M26 24h4M34 24h4" stroke-width="1.5"/>
  </svg>
  <h3>Save Money</h3>
  <p>Lorem Ipsum is simply dummy text of the printing and type setting has been the industry's</p>
</div>
<div class="feature" style="left:608px">
  <svg width="66" height="70" viewBox="0 0 66 70" fill="none" stroke="var(--orange)" stroke-width="2.5" stroke-linejoin="round">
    <path d="M33 4c10 6 18 8 28 8v20c0 16-12 28-28 34C17 60 5 48 5 32V12c10 0 18-2 28-8z"/>
    <circle cx="33" cy="35" r="13"/>
    <path d="m27 35 4 4 8-8"/>
  </svg>
  <h3>25-year warranty</h3>
  <p>Lorem Ipsum is simply dummy text of the printing and type setting has been the industry's</p>
</div>
<div class="feature" style="left:872px">
  <svg width="66" height="66" viewBox="0 0 66 66" fill="none" stroke="var(--orange)" stroke-width="2.5" stroke-linejoin="round">
    <circle cx="9" cy="9" r="5"/>
    <path d="m13 13 26 26"/>
    <path d="m36 42 6-6 18 18a4 4 0 0 1-6 6z"/>
  </svg>
  <h3>Installation Included</h3>
  <p>Lorem Ipsum is simply dummy text of the printing and type setting has been the industry's</p>
</div>

<section class="about"></section>
<h2 class="about-title">About<br>Varnek Power Services</h2>
<div class="about-copy">
  <p>Lorem Ipsum is simply dummy text of the printing and typesetting industry. Lorem Ipsum has been the industry's standard dummy text ever since the 1500s, when an unknown printer.</p>
  <p>Lorem Ipsum is simply dummy text of the printing and typesetting industry. Lorem Ipsum has been the industry's standard dummy text ever since the 1500s, when an unknown printer took a galley of type and scrambled it to make a type specimen book.</p>
</div>
<div class="btn" style="left:106px;top:1493px;width:171px;height:51px">Learn More</div>
<div class="photo" style="left:633px;top:1164px;width:489px;height:365px;background:linear-gradient(160deg,#5fa8e6 0%,#9cd0f2 35%,#b8593a 60%,#2f3f66 80%,#6a4a3a 100%)" role="img" aria-label="Brick house with a solar panel roof and wind turbines against a blue sky"></div>

<h2 class="section-title" style="left:443px;top:1668px">Our Saervices</h2>
<p class="services-lead">Lorem Ipsum is simply dummy text of the printing and typesetting industry.</p>

<div class="tile" style="left:0">
  <div class="tile-photo" role="img" aria-label="Installers talking with a homeowner beside a house with solar panels" style="background:linear-gradient(180deg,#8cb7e0 0%,#3d5d8a 45%,#8a7660 100%)"></div>
  <div class="tile-label">Consultation</div>
</div>
<div class="tile featured" style="left:241px">
  <div class="tile-photo" role="img" aria-label="Designer reviewing solar plans with a phone and light bulbs on a desk" style="background:linear-gradient(160deg,#5a7fb0 0%,#dfe6ee 40%,#f4f6f8 70%,#9aa4b0 100%)"></div>
  <div class="tile-label">Design</div>
</div>
<div class="tile" style="left:481px">
  <div class="tile-photo" role="img" aria-label="Couple standing in front of their house" style="background:linear-gradient(180deg,#c9c6bf 0%,#6f7a6a 50%,#4b7a3c 100%)"></div>
  <div class="tile-label">Permitting</div>
</div>
<div class="tile" style="left:721px">
  <div class="tile-photo" role="img" aria-label="Worker in a hard hat installing solar panels" style="background:linear-gradient(180deg,#6c85b0 0%,#9aabc8 45%,#7b8cab 100%)"></div>
  <div class="tile-label">Installation</div>
</div>
<div class="tile" style="left:962px">
  <div class="tile-photo" role="img" aria-label="Modern house with solar roof at dusk" style="background:linear-gradient(180deg,#c9dbee 0%,#3b5378 40%,#a57a52 75%,#e8d8c0 100%)"></div>
  <div class="tile-label">Activation</div>
</div>

<div class="photo" style="left:124px;top:2209px;width:490px;height:301px;background:linear-gradient(120deg,#3f6b2a 0%,#7aa04a 45%,#5e6fb0 70%,#c9d2ec 100%)" role="img" aria-label="Family standing by a fence next to a large solar panel array"></div>
<h2 class="choose-title">CHOOSE<br>INNOVATION<br><span class="accent">CHOOSE LIFE !</span></h2>
<p class="choose-copy">Lorem Ipsum is simply dummy text of the printing and typesetting industry. Lorem Ipsum has been the industry's standard dummy text ever since the 1500s, when an unknown printer took a galley of type and scrambled it to make a type specimen book.</p>

<div class="contact-fade" role="img" aria-label="Faint wind turbine field"></div>
<h2 class="section-title" style="left:469px;top:2597px">Contact Us</h2>
<p class="contact-lead">If you need an Have Any Question For Contact Us Today <a>123 456 7890.</a></p>

<span class="field-label" style="left:262px;top:2697px">Name *</span>
<div class="field" style="left:262px;top:2725px;width:333px;height:51px"></div>
<span class="field-label" style="left:618px;top:2697px">Phone *</span>
<div class="field" style="left:616px;top:2725px;width:333px;height:51px"></div>
<span class="field-label" style="left:262px;top:2790px">Email *</span>
<div class="field" style="left:262px;top:2818px;width:333px;height:51px"></div>
<span class="field-label" style="left:618px;top:2790px">Services *</span>
<div class="field" style="left:616px;top:2818px;width:333px;height:51px"></div>
<span class="field-label" style="left:262px;top:2884px">Message *</span>
<div class="field" style="left:262px;top:2912px;width:687px;height:92px"></div>
<div class="btn" style="left:532px;top:3017px;width:136px;height:51px">Send Us</div>

<footer class="site-footer"></footer>
<div class="footer-brand"><span class="brand-dot"></span><span class="brand-name">Varnek<br>Power<br>Services</span></div>
<span class="social" style="left:131px"></span>
<span class="social" style="left:178px"></span>
<span class="social" style="left:226px"></span>

<div class="footer-col" style="left:347px">
  <h4>Sitemap</h4>
  <ul><li>Home</li><li>Why Solar</li><li>Our Services</li><li>About Us</li><li>Contact Us</li></ul>
</div>
<div class="footer-col" style="left:612px">
  <h4>Support</h4>
  <ul><li>Customer Feedback</li><li>Learning Center</li><li>Verify Consultant</li><li>Contact Us</li><li>FAQs</li></ul>
</div>
<div class="footer-col" style="left:878px">
  <h4>Contact Info</h4>
  <div class="contact-row">
    <svg width="24" height="30" viewBox="0 0 24 30" fill="none" stroke="var(--orange)" stroke-width="1.8"><path d="M12 28S2 17 2 11a10 10 0 0 1 20 0c0 6-10 17-10 17z"/><circle cx="12" cy="11" r="4"/></svg>
    <span>VPS<br>101 - Lorem ipsum simple<br>Text of Print industry,</span>
  </div>
  <div class="contact-row">
    <svg width="24" height="24" viewBox="0 0 24 24" fill="none" stroke="var(--orange)" stroke-width="1.6"><path d="M6.6 10.8a15 15 0 0 0 6.6 6.6l2.2-2.2a1 1 0 0 1 1-.25 11.4 11.4 0 0 0 3.6.57 1 1 0 0 1 1 1V20a1 1 0 0 1-1 1A17 17 0 0 1 3 4a1 1 0 0 1 1-1h3.5a1 1 0 0 1 1 1c0 1.25.2 2.45.57 3.57a1 1 0 0 1-.25 1z"/></svg>
    <span>123 456 7890</span>
  </div>
  <div class="contact-row">
    <svg width="26" height="20" viewBox="0 0 26 20" fill="none" stroke="var(--orange)" stroke-width="1.6"><rect x="1" y="2" width="24" height="16"/><path d="m1 2 12 9 12-9"/></svg>
    <span>info@varnekpower.com</span>
  </div>
</div>

<div class="copyright">©2019 <span class="accent">VPS</span> - All rights Reserved. | Privacy Policy | Terms &amp; Conditions</div>

</body>
</html>
```